Income Tax Business Cards - Updates

Need to update these business cards while keeping all the same wording but just update them and make them look nicer and more modern/ on brand with our brand.

Industry/Entity Type

finance

Contact Information for Business Card

we have multiple locations so will just need to easily be able to change the address and phone numbers

Colors

Designer to choose colors to be used in the design.

```html
<!DOCTYPE html>
<html lang="en">
<head>
<meta charset="UTF-8">
<title>Tax Service Business Cards</title>
<link rel="stylesheet" href="https://fonts.googleapis.com/css2?family=Oswald:wght@500;700&family=Montserrat:wght@400;600;700&display=swap">
<style>
  :root {
    --green: #1f5e3a;
    --green-dark: #174a2d;
    --red: #d3262e;
    --red-dark: #b51d24;
    --gold: #f0a13a;
    --white: #ffffff;
    --ink: #2a2a2a;
    --stage: #e9e9e7;
  }
  * { margin: 0; padding: 0; box-sizing: border-box; }
  html, body { width: 1200px; height: 800px; overflow: hidden; }
  body {
    background: var(--stage);
    display: flex;
    align-items: center;
    justify-content: center;
    gap: 50px;
  }
  .card {
    position: relative;
    width: 525px;
    height: 300px;
    border-radius: 18px;
    overflow: hidden;
    box-shadow: 0 10px 26px rgba(0,0,0,0.18);
  }

  /* Front */
  .card--front { background: var(--green); }
  .front__badge {
    position: absolute;
    top: 0;
    right: 28px;
    width: 160px;
    height: 130px;
  }
  .front__badge-shape {
    position: absolute;
    inset: 0;
    width: 100%;
    height: 100%;
  }
  .front__badge-text {
    position: absolute;
    top: 12px;
    left: 0;
    width: 100%;
    text-align: center;
    color: var(--white);
    font-family: "Oswald", sans-serif;
    font-weight: 700;
    text-transform: uppercase;
    line-height: 1;
  }
  .front__badge-text .big { display: block; font-size: 46px; }
  .front__badge-text .small { display: block; font-size: 21px; margin-top: 2px; }
  .front__offer {
    position: absolute;
    left: 30px;
    top: 62px;
    color: var(--white);
    font-family: "Oswald", sans-serif;
    font-weight: 700;
    text-transform: uppercase;
    line-height: 1.05;
  }
  .front__offer .amount { display: block; font-size: 40px; }
  .front__offer .advance { display: block; font-size: 27px; }
  .front__offer .terms { display: block; font-size: 14px; font-weight: 500; margin-top: 3px; letter-spacing: 0.3px; }
  .front__band {
    position: absolute;
    left: 0;
    top: 188px;
    width: 100%;
    height: 88px;
    background: var(--white);
    padding: 8px 30px;
    color: var(--red);
    font-family: "Oswald", sans-serif;
    font-weight: 700;
    font-size: 34px;
    line-height: 1.05;
    text-transform: uppercase;
  }

  /* Back */
  .card--back { background: var(--white); }
  .back__pattern {
    position: absolute;
    left: 0;
    bottom: 0;
    width: 190px;
    height: 100%;
    background: linear-gradient(90deg, rgba(31,94,58,0.55) 0%, rgba(31,94,58,0.25) 55%, rgba(31,94,58,0) 100%);
  }
  .back__content {
    position: absolute;
    left: 205px;
    top: 40px;
    right: 24px;
  }
  .brand {
    display: flex;
    align-items: center;
    gap: 10px;
    font-family: "Montserrat", sans-serif;
    font-weight: 700;
    color: var(--green);
    font-size: 20px;
    line-height: 1.15;
  }
  .brand__mark {
    width: 14px;
    height: 14px;
    border-radius: 50%;
    background: var(--red);
    flex: none;
  }
  .phone {
    display: flex;
    align-items: center;
    gap: 10px;
    margin-top: 26px;
    color: var(--red);
    font-family: "Oswald", sans-serif;
    font-weight: 700;
    font-size: 36px;
    line-height: 1;
  }
  .phone svg { width: 26px; height: 26px; flex: none; }
  .address {
    margin-top: 16px;
    font-family: "Montserrat", sans-serif;
    font-size: 15px;
    color: var(--ink);
    line-height: 1.35;
    font-style: normal;
  }
</style>
</head>
<body>
  <section class="card card--front">
    <div class="front__badge">
      <svg class="front__badge-shape" viewBox="0 0 160 130" aria-hidden="true">
        <path d="M0 0 H160 V95 L80 130 L0 95 Z" fill="var(--red)"/>
        <path d="M8 0 V90 L80 121 L152 90 V0" fill="none" stroke="var(--gold)" stroke-width="1.5"/>
      </svg>
      <p class="front__badge-text">
        <span class="big">Free</span>
        <span class="small">Estimates!</span>
      </p>
    </div>
    <p class="front__offer">
      <span class="amount">Up to $6,000</span>
      <span class="advance">Same Day Advance</span>
      <span class="terms">On approved tax returns!</span>
    </p>
    <p class="front__band">File Your<br>Taxes Here</p>
  </section>

  <section class="card card--back">
    <div class="back__pattern" role="img" aria-label="Scattered green dollar sign pattern"></div>
    <div class="back__content">
      <div class="brand">
        <span class="brand__mark"></span>
        <span>Ledgerline Financial Group</span>
      </div>
      <div class="phone">
        <svg viewBox="0 0 24 24" aria-hidden="true"><path fill="var(--red)" d="M6.6 10.8a15.1 15.1 0 0 0 6.6 6.6l2.2-2.2a1 1 0 0 1 1-.25 11.4 11.4 0 0 0 3.6.57 1 1 0 0 1 1 1V20a1 1 0 0 1-1 1A17 17 0 0 1 3 4a1 1 0 0 1 1-1h3.5a1 1 0 0 1 1 1c0 1.25.2 2.45.57 3.57a1 1 0 0 1-.25 1Z"/></svg>
        <span>(555)555-5555</span>
      </div>
      <address class="address">
        Address Line 1,<br>
        Address Line 2,<br>
        Address Line 3.
      </address>
    </div>
  </section>
</body>
</html>
```